Business card for a doctor's practice

Would like a business card for a Pulmonary ( lung) doctor. I would like to include a logo with something in reference to air or oxygen or lungs. Would like the color red included somehow. Name of the company is Breathwell Medical Associates of Eastern Ridgeford and we specialize in Pulmonary Medicine,. I would like something streamlined and modern
Target Market(s)
Patients, hospitals, other doctors
Industry/Entity Type
Business
Contact Information for Business Card
Would like business details superimposed on a logo somehow

```html
<!DOCTYPE html>
<html lang="en">
<head>
<meta charset="utf-8">
<title>Breathwell Medical Associates – Business Card</title>
<link href="https://fonts.googleapis.com/css2?family=Source+Sans+3:wght@400;600&display=swap" rel="stylesheet">
<style>
  :root {
    --backdrop: #2a2a2a;
    --card: #141414;
    --card-edge: #1f1f1f;
    --red: #e3191f;
    --text: #e6e6e6;
    --rule: #3a3a3a;
  }
  * { box-sizing: border-box; margin: 0; padding: 0; }
  html, body {
    width: 1200px; height: 900px; overflow: hidden;
    background: var(--backdrop);
    font-family: "Source Sans 3", "Myriad Pro", Arial, sans-serif;
  }
  .stage {
    position: relative; width: 1200px; height: 900px;
    display: flex; align-items: center; justify-content: center; gap: 40px;
  }
  .card {
    width: 520px; height: 300px;
    background: var(--card);
    border: 1px solid var(--card-edge);
    border-radius: 18px;
    box-shadow: 0 14px 30px rgba(0,0,0,.45);
    position: relative;
  }
  /* Contact side */
  .card--contact { display: flex; }
  .brand-panel {
    width: 46%;
    display: flex; flex-direction: column; align-items: center; justify-content: center; gap: 14px;
    padding: 0 20px;
  }
  .brand-dot {
    width: 64px; height: 64px; border-radius: 50%;
    border: 6px solid var(--red);
  }
  .brand-name {
    color: var(--red); font-weight: 600; font-size: 17px; line-height: 1.2;
    text-align: center;
  }
  .divider {
    width: 1px; margin: 30px 0;
    background: var(--rule);
  }
  .details {
    flex: 1; padding: 40px 24px 0 26px;
    color: var(--text); font-size: 14px; line-height: 1.25;
  }
  .person-name { color: var(--red); font-size: 22px; font-weight: 400; line-height: 1.1; }
  .person-role { font-size: 14px; margin-bottom: 16px; }
  .address { margin-bottom: 16px; }
  .contact-list { list-style: none; display: flex; flex-direction: column; gap: 6px; }
  .contact-list li { display: flex; align-items: center; gap: 12px; }
  .contact-list svg { width: 11px; height: 11px; fill: var(--red); flex: none; }
  /* Brand side */
  .card--brand {
    display: flex; align-items: center; justify-content: center; padding: 0 50px;
  }
  .brand-title {
    color: var(--red); font-weight: 400; font-size: 30px; line-height: 1.2;
    text-align: center; letter-spacing: .5px;
  }
</style>
</head>
<body>
<main class="stage">
  <section class="card card--contact">
    <div class="brand-panel">
      <span class="brand-dot"></span>
      <p class="brand-name">Breathwell Medical Associates of Eastern Ridgeford</p>
    </div>
    <div class="divider"></div>
    <div class="details">
      <h1 class="person-name">Daniel Hartwell</h1>
      <p class="person-role">Managing Director</p>
      <p class="address">12345, Address Goes Here<br>Country Name, 123456</p>
      <ul class="contact-list">
        <li>
          <svg viewBox="0 0 24 24" aria-hidden="true"><path d="M6.6 10.8a15 15 0 0 0 6.6 6.6l2.2-2.2c.3-.3.7-.4 1-.2 1.1.4 2.3.6 3.6.6.6 0 1 .4 1 1V20c0 .6-.4 1-1 1A17 17 0 0 1 3 4c0-.6.4-1 1-1h3.5c.6 0 1 .4 1 1 0 1.3.2 2.5.6 3.6.1.3 0 .7-.2 1z"/></svg>
          (044)-555-0182
        </li>
        <li>
          <svg viewBox="0 0 24 24" aria-hidden="true"><path d="M7 1h10a2 2 0 0 1 2 2v18a2 2 0 0 1-2 2H7a2 2 0 0 1-2-2V3a2 2 0 0 1 2-2zm0 3v14h10V4z"/></svg>
          123-555-0147
        </li>
        <li>
          <svg viewBox="0 0 24 24" aria-hidden="true"><path d="M2 5h20v14H2zm2 2v.5l8 5 8-5V7z"/></svg>
          info@breathwellmed.com
        </li>
        <li>
          <svg viewBox="0 0 24 24" aria-hidden="true"><circle cx="12" cy="12" r="10"/></svg>
          www.breathwellmed.com
        </li>
      </ul>
    </div>
  </section>

  <section class="card card--brand">
    <h2 class="brand-title">Breathwell Medical Associates of Eastern Ridgeford</h2>
  </section>
</main>
</body>
</html>
```